WordPress Site Design and Code for Technology Consulting Startup

We need a WordPress design and code to a new site on Nimbo Vault. We have the logo and colors ready. The site will be a brochure site with a CONTACT page that contains a form that the prospective client fills out. The other pages would be ABOUT / SERVICES (3 option drop-down) / SUPPORT. The site should be appropriate for an IT Consulting / IT Managed Services / IT Project Management services in the Chicago area.

Target Market(s)

Across small, medium, large businesses.

Industry/Entity Type

Technology, network infrastructure, IT.

Coding

Coded - Design and coding required

Number of Pages Required

5+ page

Requirements
Nice to have
• I prefer mid-modern / simple / art deco / minimalist.

```html
<!DOCTYPE html>
<html lang="en">
<head>
<meta charset="UTF-8">
<title>Corvane Consulting – IT Consulting Services</title>
<link rel="stylesheet" href="https://fonts.googleapis.com/css2?family=Michroma&family=Orbitron:wght@800;900&family=Montserrat:wght@400;500;600&display=swap">
<style>
  :root{
    --teal:#0b93ad;
    --teal-dark:#087a90;
    --orange:#f47c20;
    --ink:#1d1d1d;
    --text:#333;
    --grey-btn:#a9a9a9;
    --field-line:#d4dbe0;
    --footer:#23272b;
    --white:#fff;
  }
  *{box-sizing:border-box;margin:0;padding:0}
  html,body{width:1200px;height:3133px;overflow:hidden}
  body{position:relative;background:var(--white);font-family:"Montserrat",sans-serif;color:var(--text)}
  .abs{position:absolute}

  /* brand */
  .brand{position:absolute;font-family:"Montserrat",sans-serif;font-weight:600;color:var(--teal);letter-spacing:3px;display:flex;align-items:center;gap:10px;line-height:1}
  .brand .mark{width:18px;height:18px;background:var(--orange)}
  .header-brand{left:88px;top:33px;font-size:28px}
  .footer-brand{left:0;width:1200px;justify-content:center;top:2848px;font-size:34px;z-index:2}

  /* header */
  .main-nav a{position:absolute;top:40px;font-family:"Michroma",sans-serif;font-size:12px;color:var(--ink);text-decoration:none;letter-spacing:.5px}
  .main-nav a.active{color:var(--orange)}
  .main-nav a.active::after{content:"";position:absolute;left:0;right:0;bottom:-6px;height:2px;background:var(--orange)}
  .btn{position:absolute;display:flex;align-items:center;justify-content:center;font-family:"Michroma",sans-serif;font-size:12px;color:var(--white);letter-spacing:.5px;text-decoration:none;z-index:2}
  .btn-teal{background:var(--teal);outline:2px solid var(--teal);outline-offset:2px;border:1px solid var(--white)}
  .btn-orange{background:var(--orange);outline:2px solid var(--orange);outline-offset:2px;border:1px solid var(--white)}
  .btn-grey{background:var(--grey-btn);outline:2px solid #c9c9c9;outline-offset:2px;border:1px solid var(--white)}

  /* hero */
  .hero{left:0;top:94px;width:1200px;height:503px;background:linear-gradient(100deg,#4a4f55 0%,#6b6f72 30%,#3c4148 60%,#5c6166 100%)}
  .hero::after{content:"";position:absolute;inset:0;background:rgba(20,24,28,.35)}
  .hero-title{position:absolute;left:0;width:1200px;top:254px;text-align:center;font-family:"Orbitron",sans-serif;font-weight:900;font-size:46px;line-height:57px;color:var(--white);letter-spacing:2px;z-index:2}
  .dot{position:absolute;top:566px;width:14px;height:14px;border:2px solid var(--white);border-radius:50%;z-index:2}
  .dot.on{border-color:var(--orange)}
  .dot.on::after{content:"";position:absolute;left:3px;top:3px;width:4px;height:4px;border-radius:50%;background:var(--orange)}

  /* intro */
  .section-title{font-family:"Orbitron",sans-serif;font-weight:900;color:var(--teal);letter-spacing:1px}
  .intro-title{left:88px;top:670px;width:480px;font-size:32px;line-height:40px;letter-spacing:2.5px}
  .rule{position:absolute;height:2px;background:var(--teal)}
  .intro-copy{left:599px;top:674px;width:500px;font-size:14px;line-height:21px;color:var(--ink)}
  .intro-copy p+p{margin-top:21px}

  .center-title{left:0;width:1200px;text-align:center;font-size:33px}

  /* services */
  .services-band{left:0;top:1147px;width:1200px;height:1042px;background:var(--teal)}
  .photo-frame{position:absolute;border:3px solid #c8ccd0}
  .photo{position:absolute}
  .svc-title{position:absolute;font-family:"Montserrat",sans-serif;font-weight:600;font-size:24px;color:var(--white)}
  .svc-copy{position:absolute;font-size:13px;line-height:19px;color:var(--white);width:400px}
  .right{text-align:right}

  /* form */
  .field{position:absolute;border:1px solid var(--field-line);display:flex;align-items:flex-start;padding:14px 0 0 16px;font-size:13px;color:#9aa3a8;gap:12px}
  .field svg{flex:none}

  /* footer */
  .site-footer{left:0;top:2736px;width:1200px;height:397px;background:linear-gradient(110deg,#2c3035,#1c1f22 50%,#2a2e33)}
  .contact-bar{left:107px;top:2909px;width:985px;height:82px;background:var(--white)}
  .contact-item{position:absolute;display:flex;align-items:center;gap:12px;font-size:13.5px;color:var(--ink);line-height:19px}
  .social{position:absolute;top:2942px;width:14px;height:14px;border-radius:50%;background:#c4c8cb}
  .social.on{top:2935px;width:28px;height:28px;background:var(--orange)}
  .footer-nav a{position:absolute;top:3027px;font-family:"Michroma",sans-serif;font-size:12px;color:var(--white);text-decoration:none}
  .footer-nav a.active{color:var(--orange)}
  .footer-nav a.active::after{content:"";position:absolute;left:0;right:0;bottom:-5px;height:2px;background:var(--orange)}
  .copyright{left:0;width:1200px;top:3062px;text-align:center;font-size:13px;color:var(--white)}
  .to-top{left:1047px;top:3050px;width:34px;height:34px;border:1.5px solid #8d9296;border-radius:50%}
</style>
</head>
<body>

<header class="site-header">
  <div class="brand header-brand"><span class="mark"></span>CORVANE</div>
  <nav class="main-nav">
    <a class="active" style="left:459px">HOME</a>
    <a style="left:547px">ABOUT US</a>
    <a style="left:673px">SERVICES</a>
    <a style="left:793px">CONTACT US</a>
  </nav>
  <a class="btn btn-teal" style="left:943px;top:31px;width:166px;height:34px;font-size:13px">GET IN TOUCH</a>
</header>

<section class="abs hero" role="img" aria-label="Photo of a business team in suits talking and smiling in a meeting"></section>
<h1 class="hero-title">IT CONSULTING<br>SERVICES</h1>
<a class="btn btn-orange" style="left:532px;top:389px;width:136px;height:32px">READ MORE</a>
<span class="dot" style="left:563px"></span>
<span class="dot on" style="left:592px"></span>
<span class="dot" style="left:620px"></span>

<h2 class="abs section-title intro-title">WE ARE A YOUNG MANAGEMENT IT CONSULTING</h2>
<span class="rule" style="left:88px;top:796px;width:88px"></span>
<div class="abs intro-copy">
  <p>Lorem Ipsum is simply dummy text of the printing and typesetting industry. Lorem Ipsum has been the industry's standard dummy text ever since the 1500s, when an unknown printer took a galley of type and scrambled it to make a type specimen book.</p>
  <p>It has survived not only five centuries, but also the leap into electronic typesetting, remaining essentially unchanged. It was popularised in the 1960s with the release of Lettrix sheets containing Lorem Ipsum passages, and more recently with desktop publishing software like Pagecraft including versions of Lorem Ipsum.</p>
</div>
<a class="btn btn-teal" style="left:601px;top:910px;width:137px;height:33px">READ MORE</a>

<h2 class="abs section-title center-title" style="top:1017px">SERVICES</h2>
<span class="rule" style="left:572px;top:1057px;width:56px"></span>

<section class="abs services-band"></section>

<div class="photo-frame" style="left:96px;top:1099px;width:468px;height:354px"></div>
<div class="photo" role="img" aria-label="Photo of a consultant meeting two clients at a table in an office" style="left:88px;top:1105px;width:468px;height:355px;background:linear-gradient(120deg,#8a6e58,#c9c3ba 45%,#6f7478)"></div>
<h3 class="svc-title" style="left:644px;top:1225px">IT CONSULTING</h3>
<p class="svc-copy" style="left:644px;top:1263px">Lorem Ipsum is simply dummy text of the printing and typesetting industry. Lorem Ipsum has been the industry's standard dummy text ever since the...</p>
<a class="btn btn-grey" style="left:646px;top:1342px;width:139px;height:32px">READ MORE</a>

<div class="photo-frame" style="left:636px;top:1486px;width:468px;height:356px"></div>
<div class="photo" role="img" aria-label="Photo of a support technician with a headset reviewing a clipboard at a desk" style="left:643px;top:1480px;width:468px;height:354px;background:linear-gradient(120deg,#3b3f44,#bfc4c8 45%,#e6e8ea)"></div>
<h3 class="svc-title right" style="left:164px;width:400px;top:1586px">IT MANAGED SERVICES</h3>
<p class="svc-copy right" style="left:164px;top:1624px">Lorem Ipsum is simply dummy text of the printing and typesetting industry. Lorem Ipsum has been the industry's standard dummy text ever since the...</p>
<a class="btn btn-orange" style="left:423px;top:1703px;width:137px;height:33px">READ MORE</a>

<div class="photo-frame" style="left:88px;top:1888px;width:468px;height:356px"></div>
<div class="photo" role="img" aria-label="Photo of a project team gathered around a meeting table with laptops" style="left:96px;top:1882px;width:468px;height:355px;background:linear-gradient(120deg,#9fb3a0,#d6d9d6 40%,#5a5f63)"></div>
<h3 class="svc-title" style="left:644px;top:1956px">IT PROJECT MANAGEMENT</h3>
<p class="svc-copy" style="left:644px;top:1994px">Lorem Ipsum is simply dummy text of the printing and typesetting industry. Lorem Ipsum has been the industry's standard dummy text ever since the...</p>
<a class="btn btn-grey" style="left:646px;top:2074px;width:139px;height:32px">READ MORE</a>

<h2 class="abs section-title center-title" style="top:2315px">GET IN TOUCH</h2>
<span class="rule" style="left:572px;top:2355px;width:56px"></span>

<div class="field" style="left:303px;top:2388px;width:289px;height:38px;padding-top:11px">
  <svg width="13" height="14" viewBox="0 0 13 14" fill="none" stroke="#9aa3a8" stroke-width="1.2"><circle cx="6.5" cy="4" r="3"/><path d="M1 13c0-3 2.5-5 5.5-5s5.5 2 5.5 5"/></svg>First Name</div>
<div class="field" style="left:608px;top:2388px;width:289px;height:38px;padding-top:11px">
  <svg width="13" height="14" viewBox="0 0 13 14" fill="none" stroke="#9aa3a8" stroke-width="1.2"><circle cx="6.5" cy="4" r="3"/><path d="M1 13c0-3 2.5-5 5.5-5s5.5 2 5.5 5"/></svg>Last Name</div>
<div class="field" style="left:303px;top:2438px;width:289px;height:38px;padding-top:11px">
  <svg width="14" height="14" viewBox="0 0 14 14" fill="none" stroke="#9aa3a8" stroke-width="1.2"><rect x="1" y="3" width="12" height="8"/><path d="M1 3l6 5 6-5"/></svg>Email</div>
<div class="field" style="left:608px;top:2438px;width:289px;height:38px;padding-top:11px">
  <svg width="13" height="14" viewBox="0 0 13 14" fill="none" stroke="#9aa3a8" stroke-width="1.2"><rect x="3" y="1" width="7" height="12" rx="1"/></svg>Phone</div>
<div class="field" style="left:303px;top:2489px;width:594px;height:96px">
  <svg width="14" height="14" viewBox="0 0 14 14" fill="none" stroke="#9aa3a8" stroke-width="1.2"><path d="M1 1h12v8l-4 4H1z"/><path d="M9 13V9h4"/></svg>How can we help?</div>
<a class="btn btn-teal" style="left:548px;top:2621px;width:104px;height:33px">SUBMIT</a>

<footer class="abs site-footer" role="img" aria-label="Darkened photo of a business team meeting"></footer>
<div class="brand footer-brand"><span class="mark"></span>CORVANE</div>

<div class="abs contact-bar"></div>
<div class="contact-item" style="left:132px;top:2930px">
  <svg width="18" height="22" viewBox="0 0 18 22" fill="none" stroke="var(--teal)" stroke-width="2.4"><path d="M9 20s-7-7-7-11a7 7 0 0 1 14 0c0 4-7 11-7 11z"/><circle cx="9" cy="9" r="2.5"/></svg>
  <span>418 W. Harlow Street, Suite<br>700N, Chicago IL 60610</span>
</div>
<div class="contact-item" style="left:403px;top:2940px">
  <svg width="20" height="15" viewBox="0 0 20 15"><rect width="20" height="15" fill="var(--teal)"/><path d="M1 1l9 7 9-7M1 14l7-6M19 14l-7-6" stroke="#fff" stroke-width="1.5" fill="none"/></svg>
  <span>info@corvaneconsult.com</span>
</div>
<div class="contact-item" style="left:662px;top:2940px">
  <svg width="18" height="18" viewBox="0 0 18 18"><path d="M4 1l3 4-2 2c1 2.5 3.5 5 6 6l2-2 4 3-2 3C8 17 1 10 1 3z" fill="var(--teal)"/></svg>
  <span>312-555-0148</span>
</div>
<span class="abs" style="left:848px;top:2922px;width:1px;height:46px;background:#e2e5e7"></span>
<span class="social" style="left:910px"></span>
<span class="social" style="left:945px"></span>
<span class="social on" style="left:976px"></span>
<span class="social" style="left:1021px"></span>

<nav class="footer-nav">
  <a class="active" style="left:378px">HOME</a>
  <a style="left:466px">ABOUT US</a>
  <a style="left:592px">SERVICES</a>
  <a style="left:712px">CONTACT US</a>
</nav>
<p class="abs copyright">Copyright © 2023 Corvane Consulting. All Rights Reserved</p>
<div class="abs to-top">
  <svg width="31" height="31" viewBox="0 0 31 31" fill="none" stroke="#8d9296" stroke-width="1.5"><path d="M10 10h11M15.5 23V13M11.5 17l4-4 4 4"/></svg>
</div>

</body>
</html>
```